All Natural Mosquito Repellent

My company, BrightFern Company has created an all natural mosquito repellent. I already have other all natural products that I have developed and created labels for. I will include a copy of that label so you have something to work from. I will need two labels. One for the front of the bottle and one for the back. The back label will need space for a UPC. The labels need to be 63mm (H) x 39mm (W)

Target Market(s)

Consumers, Organic, People who like natural products

Font styles to use
Other font styles liked:
• A combination of both Serif and Sans Serif

Requirements
Must have
• Use the words Organic, All Natural, Travel size, made in the USA label
Nice to have
• tag line: Don't beat them off. Spray them away.

```html
<!DOCTYPE html>
<html lang="en">
<head>
<meta charset="utf-8">
<title>BrightFern Company – Mosquito Repellent Labels</title>
<link href="https://fonts.googleapis.com/css2?family=Anton&family=Bebas+Neue&family=Oswald:wght@500&family=Poppins:wght@400;500;600;700&display=swap" rel="stylesheet">
<style>
  :root{
    --bg:#e6e6e6;
    --paper:#ffffff;
    --forest:#1f4a22;
    --forest-deep:#123016;
    --leaf:#2f6a2c;
    --orange:#f07f2a;
    --yellow:#f4e51d;
    --gold:#d4a02b;
    --gold-light:#f1d77a;
    --ink:#4a4a4a;
    --grey:#5e5e5e;
    --red:#e42b23;
    --white:#ffffff;
  }
  *{box-sizing:border-box;margin:0;padding:0}
  html,body{width:756px;height:1200px;overflow:hidden;background:var(--bg)}
  body{position:relative;font-family:"Poppins",sans-serif}
  .label{position:absolute;top:333px;width:330px;height:534px;background:var(--paper);overflow:hidden;box-shadow:0 6px 12px rgba(0,0,0,.28)}
  .label--front{left:32px}
  .label--back{left:394px}
  .foliage{position:absolute;inset:0;width:100%;height:100%}
  .abs{position:absolute}
  .brand{display:flex;align-items:center;gap:8px}
  .brand__dot{width:34px;height:34px;border-radius:50%;background:var(--orange);flex:none}
  .brand__name{font-weight:600;font-size:19px;color:var(--grey);letter-spacing:.5px;line-height:1}
  .brand__tag{font-size:8.5px;color:var(--grey);margin-top:3px;font-style:italic}
  .brand__star{color:var(--orange)}
  .shield{position:absolute}
  .head{position:absolute;left:0;right:0;text-align:center;line-height:1}
  .head--kicker{font-family:"Bebas Neue",sans-serif;color:var(--ink)}
  .head--spray{font-family:"Anton",sans-serif;color:var(--forest)}
  .head--off{font-family:"Anton",sans-serif;color:var(--orange)}
  .mosquito{position:absolute;border-radius:50%;background:radial-gradient(ellipse at 45% 45%,#8a6a4e 0%,#6d6f86 40%,rgba(160,200,225,.6) 70%,rgba(255,255,255,0) 100%)}
  .features{position:absolute;left:0;right:0;top:368px;display:flex;justify-content:center}
  .feature{width:78px;text-align:center;font-family:"Oswald",sans-serif;font-weight:500;font-size:12px;color:var(--white)}
  .feature + .feature{border-left:1px dashed rgba(255,255,255,.7)}
  .feature svg{display:block;margin:0 auto 6px}
  .product{position:absolute;left:0;right:0;text-align:center;color:var(--yellow);font-weight:600;line-height:1}
  .product-sub{position:absolute;left:0;right:0;text-align:center;color:var(--white);line-height:1}
  .flag{width:26px;height:14px;background:linear-gradient(#c8102e 0 14%,#fff 14% 28%,#c8102e 28% 42%,#fff 42% 56%,#c8102e 56% 70%,#fff 70% 85%,#c8102e 85%);position:relative}
  .flag::before{content:"";position:absolute;left:0;top:0;width:11px;height:8px;background:#2b3a8c}
  .made{font-size:5.5px;color:var(--white);margin-top:2px;font-weight:500}
  .protect{border-radius:50%;background:var(--red);color:var(--white);display:flex;flex-direction:column;align-items:center;justify-content:center;line-height:1}
  .protect small{font-size:4px;font-weight:600}
  .protect b{font-weight:600}
  .net{color:var(--white);text-align:center;line-height:1}
  .net__title{font-size:5.5px;font-weight:500;margin-bottom:3px}
  .net__row{display:flex;align-items:center}
  .net__num{color:var(--yellow);font-weight:600;font-size:12px}
  .net__unit{font-size:6.5px}
  .net__bar{width:1px;height:18px;background:var(--white);margin:0 7px}
  .benefit{position:absolute;left:32px;right:24px;display:flex;gap:12px}
  .benefit svg{flex:none}
  .benefit h3{font-size:7.5px;font-weight:500;color:var(--orange);margin-bottom:2px}
  .benefit p{font-size:4.6px;line-height:1.4;color:var(--white);font-weight:500;text-align:justify}
  .footnote{position:absolute;left:25px;top:496px;font-size:5.6px;color:var(--white);line-height:1.35}
</style>
</head>
<body>

<!-- FRONT LABEL -->
<section class="label label--front">
  <svg class="foliage" viewBox="0 0 330 534" role="img" aria-label="Photograph of dense dark green tropical leaves">
    <defs>
      <linearGradient id="leafFront" x1="0" y1="0" x2="1" y2="1">
        <stop offset="0" stop-color="#2c5f2a"/><stop offset=".5" stop-color="#1f4a22"/><stop offset="1" stop-color="#123016"/>
      </linearGradient>
    </defs>
    <path d="M0 236 C80 200 250 200 330 250 L330 534 L0 534 Z" fill="url(#leafFront)"/>
  </svg>

  <div class="brand abs" style="left:36px;top:30px">
    <span class="brand__dot"></span>
    <div>
      <div class="brand__name">BRIGHTFERN CO.</div>
      <div class="brand__tag">crafted by hand, with love <span class="brand__star">★</span> in the U.S.A.</div>
    </div>
  </div>

  <svg class="shield" style="left:42px;top:84px" width="246" height="278" viewBox="0 0 246 278">
    <defs>
      <linearGradient id="goldFront" x1="0" y1="0" x2="1" y2="1">
        <stop offset="0" stop-color="#c98f22"/><stop offset=".5" stop-color="#f1d77a"/><stop offset="1" stop-color="#9a6a1c"/>
      </linearGradient>
    </defs>
    <path d="M123 4 L242 38 C242 150 205 222 123 274 C41 222 4 150 4 38 Z" fill="#fff" stroke="url(#goldFront)" stroke-width="7"/>
  </svg>
  <div class="head head--kicker" style="top:120px;font-size:22px">DON'T BEAT THEM OFF</div>
  <div class="head head--spray" style="top:140px;font-size:54px">SPRAY</div>
  <div class="head head--off" style="top:200px;font-size:34px">THEM OFF</div>
  <div class="mosquito" role="img" aria-label="Illustration of a mosquito" style="left:80px;top:232px;width:160px;height:100px"></div>

  <div class="features">
    <div class="feature">
      <svg width="20" height="20" viewBox="0 0 20 20" fill="var(--orange)"><path d="M10 2c-3 0-4 3-4 5 2 0 4-1 4-4zM10 2c3 0 4 3 4 5-2 0-4-1-4-4z"/><rect x="9.3" y="6" width="1.4" height="6"/><path d="M2 13h9l2 2h5v2H6z"/></svg>
      ORGANIC
    </div>
    <div class="feature">
      <svg width="20" height="20" viewBox="0 0 20 20" fill="var(--orange)"><path d="M3 17C3 7 9 3 18 3c0 9-5 14-12 13l-3 2z"/></svg>
      ALL NATURAL
    </div>
    <div class="feature">
      <svg width="20" height="20" viewBox="0 0 20 20" fill="none" stroke="var(--orange)" stroke-width="1.6"><rect x="7" y="6" width="9" height="8"/><path d="M3 2v15h15"/></svg>
      TRAVEL SIZE
    </div>
  </div>

  <div class="product" style="top:428px;font-size:16.5px">Mosquito repellent Spray</div>
  <div class="product-sub" style="top:450px;font-size:7px">Safe for kids upto 3 ages</div>

  <div class="abs" style="left:25px;top:488px">
    <div class="flag" role="img" aria-label="United States flag"></div>
    <div class="made">MADE IN USA</div>
  </div>
  <div class="protect abs" style="left:70px;top:482px;width:30px;height:30px">
    <small>PROTECTS</small><b style="font-size:8.5px">10hrs</b>
  </div>
  <div class="net abs" style="left:248px;top:484px">
    <div class="net__title">Net Weight</div>
    <div class="net__row">
      <div><div class="net__num">8</div><div class="net__unit">Ounces</div></div>
      <div class="net__bar"></div>
      <div><div class="net__num">236</div><div class="net__unit">ml</div></div>
    </div>
  </div>
</section>

<!-- BACK LABEL -->
<section class="label label--back">
  <svg class="foliage" viewBox="0 0 330 534" role="img" aria-label="Photograph of dense dark green tropical leaves">
    <defs>
      <linearGradient id="leafBack" x1="0" y1="0" x2="1" y2="1">
        <stop offset="0" stop-color="#2c5f2a"/><stop offset=".5" stop-color="#1f4a22"/><stop offset="1" stop-color="#123016"/>
      </linearGradient>
    </defs>
    <path d="M0 152 C90 118 240 112 330 134 L330 534 L0 534 Z" fill="url(#leafBack)"/>
  </svg>

  <div class="brand abs" style="left:58px;top:26px">
    <span class="brand__dot" style="width:30px;height:30px"></span>
    <div>
      <div class="brand__name" style="font-size:16.5px">BRIGHTFERN CO.</div>
      <div class="brand__tag" style="font-size:7.5px">crafted by hand, with love <span class="brand__star">★</span> in the U.S.A.</div>
    </div>
  </div>

  <svg class="shield" style="left:91px;top:76px" width="148" height="170" viewBox="0 0 246 278">
    <defs>
      <linearGradient id="goldBack" x1="0" y1="0" x2="1" y2="1">
        <stop offset="0" stop-color="#c98f22"/><stop offset=".5" stop-color="#f1d77a"/><stop offset="1" stop-color="#9a6a1c"/>
      </linearGradient>
    </defs>
    <path d="M123 4 L242 38 C242 150 205 222 123 274 C41 222 4 150 4 38 Z" fill="#fff" stroke="url(#goldBack)" stroke-width="9"/>
  </svg>
  <div class="head head--kicker" style="top:103px;font-size:13px">DON'T BEAT THEM OFF</div>
  <div class="head head--spray" style="top:113px;font-size:33px">SPRAY</div>
  <div class="head head--off" style="top:150px;font-size:21px">THEM OFF</div>
  <div class="mosquito" role="img" aria-label="Illustration of a mosquito" style="left:115px;top:175px;width:100px;height:62px"></div>

  <div class="product" style="top:256px;font-size:13.5px">Mosquito repellent Spray</div>
  <div class="product-sub" style="top:274px;font-size:8px">Safe for kids upto 3 ages</div>

  <div class="benefit" style="top:298px">
    <svg width="38" height="38" viewBox="0 0 38 38" fill="none" stroke="var(--orange)" stroke-width="3"><circle cx="19" cy="19" r="16"/><circle cx="19" cy="19" r="10"/><path d="M19 13v6l4 3"/></svg>
    <div>
      <h3>10hours protection</h3>
      <p>It is a long established fact that a reader will be distracted by the readable content of a page when looking at its layout. The point of using Lorem Ipsum is that it has a more-or-less normal distribution of letters, as opposed to using 'Content here, content here', making it look like readable English of letters, as opposed to using 'Content here, content here.</p>
    </div>
  </div>
  <div class="benefit" style="top:357px">
    <svg width="38" height="38" viewBox="0 0 38 38" fill="var(--orange)"><path d="M4 28l10-14 6 4 8-8 6 6-10 12-6-2-6 6z"/><path d="M18 6l4 4-3 3-4-4z"/></svg>
    <div>
      <h3>Skin Friendly</h3>
      <p>It is a long established fact that a reader will be distracted by the readable content of a page when looking at its layout. The point of using Lorem Ipsum is that it has a more-or-less normal distribution of letters, as opposed to using 'Content here, content here', making it look like readable English of letters, as opposed to using 'Content here, content here.</p>
    </div>
  </div>
  <div class="benefit" style="top:416px">
    <svg width="38" height="38" viewBox="0 0 38 38"><path d="M19 3l14 5c0 14-5 22-14 27C10 30 5 22 5 8z" fill="none" stroke="var(--orange)" stroke-width="3"/><path d="M19 3l14 5c0 14-5 22-14 27z" fill="var(--orange)"/></svg>
    <div>
      <h3>Safe</h3>
      <p>It is a long established fact that a reader will be distracted by the readable content of a page when looking at its layout. The point of using Lorem Ipsum is that it has a more-or-less normal distribution of letters, as opposed to using 'Content here, content here', making it look like readable English of letters, as opposed to using 'Content here, content here.</p>
    </div>
  </div>

  <div class="footnote">For highly chaffed, distressed, distraught,<br>or parched wood needing moisture and rejuvenation.</div>
  <div class="abs" style="left:250px;top:490px">
    <div class="flag" role="img" aria-label="United States flag"></div>
    <div class="made" style="font-size:4.5px">MADE IN USA</div>
  </div>
  <div class="protect abs" style="left:283px;top:486px;width:22px;height:22px">
    <small style="font-size:3px">PROTECTS</small><b style="font-size:6.5px">10hrs</b>
  </div>
</section>

</body>
</html>
```